Business Cards

Need a neat design for a new business card

Industry/Entity Type

Residential Construction

Contact Information for Business Card

Company Name- KORV Construction Inc.
Owner- Daniel Pruitt
Phone number- (555)270-4418
Email- korvcobuilds@mailbox-example.com
Facebook- www.socialpage-example.com/korvcobuilds

Colors
fefdec

```html
<!DOCTYPE html>
<html lang="en">
<head>
<meta charset="UTF-8">
<title>KORV Construction – Business Card</title>
<link rel="stylesheet" href="https://fonts.googleapis.com/css2?family=Arimo:wght@400;700&family=Cormorant+Garamond:wght@500&family=Noto+Serif:wght@700&display=swap">
<style>
  :root {
    --backdrop: #3c3c3e;
    --card: #1c1c1e;
    --card-edge: #2a2a2d;
    --cream: #fefdec;
    --emboss: #6d6d70;
    --band: #3a3e43;
    --band-tab: #474c52;
  }
  * { margin: 0; padding: 0; box-sizing: border-box; }
  html, body { width: 799px; height: 1200px; overflow: hidden; }
  body {
    background: var(--backdrop);
    position: relative;
    font-family: "Arimo", Arial, sans-serif;
  }
  .card {
    position: absolute;
    left: 100px;
    width: 600px;
    height: 343px;
    background: var(--card);
    border: 1px solid var(--card-edge);
    border-radius: 4px;
    overflow: hidden;
    box-shadow: 0 14px 30px rgba(0,0,0,0.45);
  }
  .card--front { top: 155px; }
  .card--back { top: 700px; }

  /* Front */
  .front-name {
    position: absolute;
    left: 0; right: 0; top: 118px;
    display: flex; align-items: center; justify-content: center; gap: 16px;
    font-family: "Cormorant Garamond", Georgia, serif;
    font-weight: 500;
    color: var(--emboss);
    font-size: 58px;
    letter-spacing: 6px;
    line-height: 1;
  }
  .front-name .mark-square {
    width: 14px; height: 14px; background: var(--emboss);
  }
  .front-tagline {
    position: absolute; left: 0; right: 0; top: 190px;
    text-align: center;
    font-family: "Cormorant Garamond", Georgia, serif;
    font-weight: 500;
    color: var(--emboss);
    font-size: 17px;
    letter-spacing: 6px;
  }

  /* Back */
  .brand {
    position: absolute; left: 40px; top: 34px;
    display: flex; align-items: center; gap: 12px;
    font-family: "Cormorant Garamond", Georgia, serif;
    font-weight: 500;
    color: var(--cream);
    font-size: 40px;
    letter-spacing: 3px;
    line-height: 1;
  }
  .brand .mark-square { width: 12px; height: 12px; background: var(--cream); }
  .brand-sub {
    position: absolute; left: 64px; top: 80px;
    font-family: "Cormorant Garamond", Georgia, serif;
    font-weight: 500;
    color: var(--cream);
    font-size: 16px;
    letter-spacing: 4px;
  }
  .owner { position: absolute; left: 40px; top: 128px; color: var(--cream); }
  .owner-name { font-size: 22px; }
  .owner-role { font-size: 11px; margin-top: 2px; }
  .contact {
    position: absolute; left: 300px; top: 184px;
    list-style: none; color: var(--cream); font-size: 14px;
  }
  .contact li { display: flex; align-items: center; gap: 10px; height: 22px; }
  .contact svg { width: 14px; height: 14px; flex: none; }
  .social-square { width: 11px; height: 11px; margin: 0 1.5px; background: var(--cream); flex: none; }
  .footer-band { position: absolute; left: 0; bottom: 0; width: 600px; height: 110px; }
  .footer-label {
    position: absolute; left: 185px; bottom: 30px;
    font-family: "Noto Serif", Georgia, serif; font-weight: 700;
    font-size: 14px; color: var(--cream);
  }
</style>
</head>
<body>
  <section class="card card--front" aria-label="Card front">
    <div class="front-name"><span class="mark-square"></span>KORV</div>
    <div class="front-tagline">CONSTRUCTION</div>
  </section>

  <section class="card card--back" aria-label="Card back">
    <div class="brand"><span class="mark-square"></span>KORV</div>
    <div class="brand-sub">CONSTRUCTION</div>

    <div class="owner">
      <div class="owner-name">Daniel Pruitt</div>
      <div class="owner-role">Owner</div>
    </div>

    <svg class="footer-band" viewBox="0 0 600 110" aria-hidden="true">
      <path d="M0 18 L150 30 L170 48 L600 62 L600 110 L0 110 Z" fill="var(--band)"/>
      <path d="M170 48 L600 62 L600 68 L175 54 Z" fill="var(--band-tab)"/>
    </svg>

    <ul class="contact">
      <li>
        <svg viewBox="0 0 24 24"><path fill="var(--cream)" d="M6.6 10.8a15 15 0 0 0 6.6 6.6l2.2-2.2a1 1 0 0 1 1-.25 11.4 11.4 0 0 0 3.6.6 1 1 0 0 1 1 1V20a1 1 0 0 1-1 1A17 17 0 0 1 3 4a1 1 0 0 1 1-1h3.5a1 1 0 0 1 1 1c0 1.25.2 2.45.6 3.6a1 1 0 0 1-.25 1z"/></svg>
        (555)270-4418
      </li>
      <li><span class="social-square"></span>/korvcobuilds</li>
      <li>
        <svg viewBox="0 0 24 24"><rect x="2" y="5" width="20" height="14" fill="var(--cream)"/><path d="M2 5 L12 13 L22 5" fill="none" stroke="var(--card)" stroke-width="1.6"/></svg>
        korvcobuilds@mailbox-example.com
      </li>
    </ul>

    <div class="footer-label">KORV Construction Inc.</div>
  </section>
</body>
</html>
```